Safety Company in need of a Tri-fold Brochure design

We need a tri-fold brochure for our technicians to hand out to clients. We need to show the services we provide. Design, engineering, fabrication, installation, testing, Operating/Work procedures, training, certification of Fall Protection/Window Cleaning Equipment.

Target Market(s)

building owners, property managers

Industry/Entity Type

It Company

Font styles to use
Sans Serif
Script

Colors
0455a3
ec1f27
ffffff

Requirements
Must have
• mission statement, 24 hour response policy, photos of services

```html
<!DOCTYPE html>
<html lang="en">
<head>
<meta charset="utf-8">
<title>Crestline Safety – Tri-fold Brochure</title>
<link href="https://fonts.googleapis.com/css2?family=Bebas+Neue&family=Signika:wght@500&family=Arimo:wght@400;700&display=swap" rel="stylesheet">
<style>
  :root{
    --blue:#0455a3;
    --blue-mid:#2f74b8;
    --blue-light:#3a86c8;
    --red:#ec1f27;
    --white:#ffffff;
    --ink:#111111;
    --grey-1:#f2f2f2;
    --grey-2:#d9dadc;
    --frame:#3d4350;
  }
  *{box-sizing:border-box;margin:0;padding:0}
  html,body{width:1200px;height:853px;overflow:hidden;background:var(--white)}
  .brochure{position:relative;width:1200px;height:853px;display:flex;font-family:"Arimo",Arial,sans-serif}
  .panel{position:relative;width:400px;height:853px;overflow:hidden}

  /* services panel */
  .panel--services{background:radial-gradient(circle at 40% 45%,var(--white) 0%,var(--grey-1) 45%,var(--grey-2) 100%)}
  .tab{position:absolute;left:0;top:18px;width:375px;height:42px;background:var(--blue-mid);border-radius:0 21px 21px 0;
       color:var(--white);font-family:"Signika",sans-serif;font-weight:500;font-size:21px;line-height:42px;padding-left:17px;word-spacing:5px}
  .intro{position:absolute;left:14px;top:64px;width:372px;font-weight:700;font-size:12.4px;line-height:17.7px;color:var(--ink)}
  .intro p+p{margin-top:17px}
  .works-title{position:absolute;left:0;width:388px;top:298px;text-align:center;font-family:"Bebas Neue",sans-serif;font-weight:400;font-size:23px;color:var(--ink)}
  .works-grid{position:absolute;left:35px;top:332px;width:320px;height:482px}
  .work{position:absolute;width:150px;height:115px;border-radius:14px;background:linear-gradient(#e9eaec,#bfc2c7);padding:5px;border:1px solid #9a9ea6}
  .work__photo{width:100%;height:100%;border-radius:10px;border:4px solid var(--frame)}
  .dot{position:absolute;width:34px;height:34px;border-radius:50%;background:radial-gradient(circle at 40% 35%,#ff9a9a,var(--red) 60%,#a50d12);border:3px solid var(--frame)}

  /* contact panel */
  .panel--contact{background:var(--white)}
  .mission{position:absolute;left:0;top:31px;width:400px;text-align:center;font-family:"Bebas Neue",sans-serif;font-weight:400;font-size:26px;line-height:27px;color:var(--ink)}
  .contact-card{position:absolute;left:25px;top:383px;width:353px;height:284px;background:var(--blue-mid);border-radius:14px;color:var(--white)}
  .tollfree{position:absolute;left:0;width:100%;top:17px;text-align:center;font-family:"Bebas Neue",sans-serif;font-size:31px;line-height:30px}
  .tollfree-number{position:absolute;left:84px;top:43px;font-weight:700;font-size:35px}
  .icon{position:absolute}
  .address{position:absolute;top:110px;font-weight:700;font-size:13.5px;line-height:20.5px;white-space:nowrap}
  .divider{position:absolute;left:177px;top:118px;width:2px;height:62px;background:var(--white)}
  .online{position:absolute;font-weight:700;font-size:14.5px;white-space:nowrap}
  .partners-title{position:absolute;left:0;width:400px;top:702px;text-align:center;font-weight:700;font-size:14px;letter-spacing:.3px;color:var(--ink)}
  .badge{position:absolute}

  /* cover panel */
  .panel--cover{background:var(--blue)}
  .cover-bg{position:absolute;inset:0}
  .brand{position:absolute;left:60px;width:250px;top:140px;text-align:center;font-family:"Bebas Neue",sans-serif;font-weight:400;font-size:50px;line-height:50px;color:var(--red)}
  .brand__mark{display:inline-block;width:14px;height:14px;border-radius:50%;background:var(--red);margin-right:10px;vertical-align:10px}
  .hero{position:absolute;left:88px;top:340px;width:304px;height:304px;border-radius:50%;border:12px solid var(--blue-light);
        background:linear-gradient(160deg,#e8eef4 0%,#b9c6d2 45%,#7d8c99 100%)}
  .cover-title{position:absolute;left:0;width:400px;text-align:center;color:var(--white);font-family:"Bebas Neue",sans-serif;font-weight:400;line-height:1}
  .cover-title--main{top:705px;font-size:64px}
  .cover-title--sub{top:758px;font-size:48px}
</style>
</head>
<body>
<div class="brochure">

  <section class="panel panel--services">
    <div class="tab">OPOS Documentation / Work Plan</div>
    <div class="intro">
      <p>An OPOS, or Operating Procedure Outline Sheet, verifies the equipment on the building to be used for window cleaning and exterior building maintenance procedures. Per California code, it must include a number of elements in pictorial and written form to instruct employees about safe use of roof supported building maintenance equipment and/or procedures for window cleaning.</p>
      <p>We are the industry-leader in providing OPOS documents and we develop the building specific document, as required by CA OSHA, as well as the Work Plan, a Fed OSHA required document, for exterior building maintenance equipment.</p>
    </div>
    <h2 class="works-title">Some of our works</h2>
    <div class="works-grid">
      <div class="work" style="left:0;top:0"><div class="work__photo" role="img" aria-label="Roof davit and suspended platform on a rooftop" style="background:linear-gradient(#7fa7cf,#dfe6ec 70%,#8c8f94)"></div></div>
      <div class="work" style="left:170px;top:0"><div class="work__photo" role="img" aria-label="Roof plan drawing of anchor layout" style="background:linear-gradient(135deg,#f3f5fb,#dfe4f3)"></div></div>
      <div class="work" style="left:0;top:122px"><div class="work__photo" role="img" aria-label="Technicians testing anchors beside a building" style="background:linear-gradient(#6e8a5c,#a9b59a 60%,#c8c2b4)"></div></div>
      <div class="work" style="left:170px;top:122px"><div class="work__photo" role="img" aria-label="Safety training class in a meeting room" style="background:linear-gradient(#bdb6aa,#8c8377 60%,#5b4f44)"></div></div>
      <div class="work" style="left:0;top:244px"><div class="work__photo" role="img" aria-label="Building facade with parapet wall" style="background:linear-gradient(#6b6a66,#9d9a92 55%,#d1cec6)"></div></div>
      <div class="work" style="left:170px;top:244px"><div class="work__photo" role="img" aria-label="Rooftop guardrail along building edge" style="background:linear-gradient(#aab7c4,#6f7c88 55%,#4a545e)"></div></div>
      <div class="work" style="left:0;top:366px"><div class="work__photo" role="img" aria-label="Roof anchor fixture on a terrace floor" style="background:linear-gradient(#8a5a3e,#b88a6a 55%,#6b4b38)"></div></div>
      <div class="work" style="left:170px;top:366px"><div class="work__photo" role="img" aria-label="Crew operating a suspended work platform" style="background:linear-gradient(#c9d6e2,#a3b2bf 55%,#6d7b87)"></div></div>
      <div class="dot" style="left:143px;top:73px"></div>
      <div class="dot" style="left:143px;top:195px"></div>
      <div class="dot" style="left:143px;top:317px"></div>
      <div class="dot" style="left:143px;top:439px"></div>
    </div>
  </section>

  <section class="panel panel--contact">
    <p class="mission">For over 42 years we have been doing our<br>most important duty, providing buildings<br>with a safe working environment.<br>We are proficient in finding solutions of<br>value and provide you and your workers a<br>safe work environment. Our service and<br>equipment is always state of the art and in<br>line with all regulations and certification<br>approval standards</p>

    <div class="contact-card">
      <div class="tollfree">Toll Free</div>
      <svg class="icon" style="left:20px;top:44px" width="40" height="40" viewBox="0 0 40 40" aria-hidden="true">
        <path d="M9 4 L16 3 L19 13 L14 16 Q18 26 25 31 L29 26 L38 31 L36 38 Q30 40 22 35 Q10 26 6 14 Q5 8 9 4 Z" fill="var(--white)"/>
      </svg>
      <div class="tollfree-number">(800) 555-0142</div>

      <svg class="icon" style="left:14px;top:108px" width="20" height="26" viewBox="0 0 20 26" aria-hidden="true">
        <path d="M10 0 A9 9 0 0 1 19 9 C19 15 10 26 10 26 C10 26 1 15 1 9 A9 9 0 0 1 10 0 Z" fill="var(--white)"/>
        <circle cx="10" cy="9" r="3.5" fill="var(--blue-mid)"/>
      </svg>
      <div class="address" style="left:40px;top:112px">42 Ridge Court<br>Suite B<br>Orinda, CA 94563</div>
      <div class="divider"></div>
      <svg class="icon" style="left:202px;top:112px" width="24" height="16" viewBox="0 0 24 16" aria-hidden="true">
        <rect x="1" y="1" width="22" height="14" fill="none" stroke="var(--white)" stroke-width="2"/>
        <path d="M1 1 L12 9 L23 1" fill="none" stroke="var(--white)" stroke-width="2"/>
      </svg>
      <div class="address" style="left:232px;top:108px">PO Box 18240<br>Lafayette,<br>CA 94549</div>

      <svg class="icon" style="left:87px;top:199px" width="22" height="14" viewBox="0 0 22 14" aria-hidden="true">
        <rect x="1" y="1" width="20" height="12" fill="none" stroke="var(--white)" stroke-width="2"/>
        <path d="M1 1 L11 8 L21 1" fill="none" stroke="var(--white)" stroke-width="2"/>
      </svg>
      <div class="online" style="left:116px;top:195px">info@crestlinesafety.com</div>

      <svg class="icon" style="left:94px;top:224px" width="30" height="20" viewBox="0 0 30 20" aria-hidden="true">
        <path d="M3 3 L8 2 L10 8 L7 10 Q9 14 13 17 L15 14 L18 16 L17 19 Q12 20 7 15 Q2 9 3 3 Z" fill="var(--white)"/>
        <rect x="14" y="3" width="14" height="10" fill="none" stroke="var(--white)" stroke-width="1.8"/>
        <path d="M14 3 L21 8 L28 3" fill="none" stroke="var(--white)" stroke-width="1.8"/>
      </svg>
      <div class="online" style="left:133px;top:222px">(925) 555-0178</div>

      <svg class="icon" style="left:73px;top:253px" width="22" height="22" viewBox="0 0 22 22" aria-hidden="true">
        <circle cx="11" cy="11" r="9.5" fill="none" stroke="var(--white)" stroke-width="2"/>
        <path d="M5 8 Q11 5 17 9 M4 13 Q11 17 18 13" fill="none" stroke="var(--white)" stroke-width="2"/>
      </svg>
      <div class="online" style="left:104px;top:254px">www.crestlinesafety.com</div>
    </div>

    <h3 class="partners-title">PROUD PARTNERS AND ASSOCIATIONS</h3>
    <div class="badge" role="img" aria-label="Safety engineering society badge" style="left:38px;top:726px;width:28px;height:30px;background:#6d6e70;border-radius:4px"></div>
    <div class="badge" role="img" aria-label="Safety engineering society listing" style="left:74px;top:737px;width:262px;height:10px;background:#9a9b9d;border-radius:2px"></div>
    <div class="badge" role="img" aria-label="Fall protection manufacturer badge" style="left:30px;top:776px;width:82px;height:22px;background:#1b1b1b"></div>
    <div class="badge" role="img" aria-label="Safety products partner badge" style="left:130px;top:770px;width:40px;height:42px;border:3px solid #f2c400;background:var(--white)"></div>
    <div class="badge" role="img" aria-label="Building owners association badge" style="left:186px;top:758px;width:46px;height:72px;background:var(--blue)"></div>
    <div class="badge" role="img" aria-label="Scaffold and access association badge" style="left:250px;top:772px;width:89px;height:55px;background:var(--blue)"></div>
  </section>

  <section class="panel panel--cover">
    <svg class="cover-bg" width="400" height="853" viewBox="0 0 400 853" aria-hidden="true">
      <defs>
        <linearGradient id="coverBlue" x1="0" y1="0" x2="1" y2="1">
          <stop offset="0" stop-color="#1e78c2"/>
          <stop offset="1" stop-color="#0455a3"/>
        </linearGradient>
      </defs>
      <rect width="400" height="853" fill="url(#coverBlue)"/>
      <path d="M0 90 Q120 20 280 85 Q360 120 400 250 L400 600 Q380 720 230 705 Q100 690 0 645 Z" fill="var(--white)"/>
      <path d="M0 70 Q140 0 290 70 Q240 40 150 45 Q60 50 0 95 Z" fill="var(--red)"/>
      <path d="M120 600 Q230 720 400 510 L400 540 Q260 720 120 600 Z" fill="var(--red)"/>
    </svg>
    <div class="brand"><span class="brand__mark"></span>Crestline<br>Safety</div>
    <div class="hero" role="img" aria-label="Technicians rigging a suspended window cleaning platform on a rooftop"></div>
    <h1 class="cover-title cover-title--main">Exterior Building</h1>
    <h2 class="cover-title cover-title--sub">Safety Specialist</h2>
  </section>

</div>
</body>
</html>
```